Advertisements for dental office (3"x3.75" and 3"x2")
People of all ages looking for a family dentist.
I am looking for advertisements that are clean and sophisticated. Most dental ads are cluttered looking and list all the procedures that a dentist will perform. I do not want clutter. I want an ad that speaks for itself and has a lot of emotional appeal. The ads should be simple but still catch your eye.

```html
<!DOCTYPE html>
<html lang="en">
<head>
<meta charset="utf-8">
<title>Revin Dental – Advertisements</title>
<link href="https://fonts.googleapis.com/css2?family=Cormorant+Garamond:ital,wght@0,400;0,500;0,600;1,500&display=swap" rel="stylesheet">
<style>
  :root {
    --backdrop: #3a1f14;
    --paper: #ffffff;
    --ink-grey: #6a6a6e;
    --ink-dark: #3d3d42;
    --magenta: #a3195b;
    --magenta-deep: #7d0f44;
    --photo-hair: #5a3a2c;
    --photo-skin: #d9b8a6;
    --photo-light: #eeeef0;
  }
  * { margin: 0; padding: 0; box-sizing: border-box; }
  html, body { width: 1200px; height: 650px; overflow: hidden; }
  body {
    background: var(--backdrop);
    font-family: "Cormorant Garamond", Georgia, serif;
    position: relative;
  }
  .ad { position: absolute; background: var(--paper); overflow: hidden; }

  /* ---------- square ad ---------- */
  .ad-square { left: 60px; top: 53px; width: 680px; height: 547px; }
  .ad-square .portrait {
    position: absolute; left: 0; top: 0; width: 470px; height: 547px;
    background:
      radial-gradient(ellipse 38% 30% at 48% 50%, var(--photo-skin) 0%, rgba(217,184,166,0) 100%),
      linear-gradient(90deg, var(--photo-hair) 0%, #8a6a5c 45%, var(--photo-light) 85%, var(--paper) 100%);
  }
  .ad-square .copy {
    position: absolute; left: 430px; top: 40px; width: 250px;
    text-align: center; color: var(--ink-grey);
  }
  .headline-small { font-size: 36px; letter-spacing: 2px; font-weight: 500; line-height: 1; }
  .headline-smile { font-size: 86px; color: var(--magenta); font-weight: 600; letter-spacing: 2px; line-height: 1.05; }
  .headline-tail { font-size: 34px; letter-spacing: 1px; font-weight: 500; line-height: 1.15; }

  .brand {
    display: flex; align-items: center; justify-content: center; gap: 8px;
    color: var(--magenta); font-weight: 600; font-size: 26px;
  }
  .brand-dot { width: 18px; height: 18px; border-radius: 50%; background: var(--magenta); }

  .ad-square .brand { position: absolute; left: 420px; top: 345px; width: 260px; }
  .ad-square .practice {
    position: absolute; left: 400px; top: 420px; width: 280px; text-align: center; color: var(--ink-grey);
  }
  .practice-name { font-size: 24px; font-variant: small-caps; letter-spacing: 1px; font-weight: 500; }
  .practice-address { font-size: 17px; margin-top: 4px; }
  .practice-phone { font-size: 24px; color: var(--ink-dark); font-weight: 600; margin-top: 2px; }
  .ad-square .tagline-band {
    position: absolute; left: 360px; top: 508px; width: 320px; height: 30px;
    background: linear-gradient(90deg, rgba(163,25,91,0) 0%, var(--magenta) 18%, var(--magenta-deep) 100%);
    color: var(--paper); font-style: italic; font-size: 19px; font-weight: 500;
    display: flex; align-items: center; justify-content: flex-end; padding-right: 14px;
  }

  /* ---------- tall ad ---------- */
  .ad-tall { left: 775px; top: 48px; width: 377px; height: 562px; }
  .ad-tall .copy { position: absolute; left: 0; top: 18px; width: 377px; text-align: center; color: var(--ink-grey); }
  .ad-tall .headline-line { font-size: 27px; font-style: italic; font-weight: 500; }
  .ad-tall .headline-line .smile { font-size: 54px; color: var(--magenta); font-style: normal; font-weight: 600; }
  .ad-tall .headline-sub { font-size: 26px; font-style: italic; font-weight: 500; margin-top: 2px; }
  .ad-tall .tagline-ruled {
    display: flex; align-items: center; justify-content: center; gap: 10px;
    color: var(--magenta); font-size: 15px; font-weight: 600; margin-top: 8px;
  }
  .ad-tall .tagline-ruled::before, .ad-tall .tagline-ruled::after {
    content: ""; width: 40px; height: 1px; background: var(--magenta);
  }
  .ad-tall .portrait {
    position: absolute; left: 0; top: 185px; width: 377px; height: 377px;
    background:
      radial-gradient(ellipse 30% 35% at 52% 45%, var(--photo-skin) 0%, rgba(217,184,166,0) 100%),
      linear-gradient(90deg, var(--photo-hair) 0%, #8a6a5c 50%, #cfc9c9 100%);
  }
  .ad-tall .brand { position: absolute; left: 12px; top: 460px; font-size: 20px; justify-content: flex-start; }
  .ad-tall .brand-dot { width: 14px; height: 14px; }
  .ad-tall .practice {
    position: absolute; left: 0; top: 492px; width: 377px; height: 70px;
    background: rgba(255,255,255,0.82); text-align: center; color: var(--ink-grey); padding-top: 8px;
  }
  .ad-tall .practice-name { font-size: 24px; }
  .ad-tall .practice-contact { font-size: 16px; margin-top: 2px; }
  .ad-tall .practice-contact strong { color: var(--ink-dark); font-weight: 600; font-size: 18px; }
</style>
</head>
<body>
  <section class="ad ad-square">
    <div class="portrait" role="img" aria-label="Portrait photo of a smiling young woman with long brown hair"></div>
    <div class="copy">
      <p class="headline-small">A BEAUTIFUL</p>
      <p class="headline-smile">SMILE</p>
      <p class="headline-tail">TODAY, IT'S EASIER<br>THAN EVER</p>
    </div>
    <div class="brand"><span class="brand-dot"></span>Revin Dental</div>
    <div class="practice">
      <p class="practice-name">Marcus T. Revin, DDS, PLLC</p>
      <p class="practice-address">218 West Alder Street, Brookhaven</p>
      <p class="practice-phone">555-014-2380</p>
    </div>
    <div class="tagline-band">Comprehensive Dentistry for ALL AGES</div>
  </section>

  <section class="ad ad-tall">
    <div class="copy">
      <p class="headline-line">A Beautiful <span class="smile">Smile</span></p>
      <p class="headline-sub">Today, It's Easier Than Ever</p>
      <p class="tagline-ruled">Comprehensive Dentistry for ALL AGES</p>
    </div>
    <div class="portrait" role="img" aria-label="Portrait photo of a smiling young woman with long brown hair"></div>
    <div class="brand"><span class="brand-dot"></span>Revin Dental</div>
    <div class="practice">
      <p class="practice-name">Marcus T. Revin, DDS, PLLC</p>
      <p class="practice-contact">218 West Alder Street, Brookhaven | <strong>555-014-2380</strong></p>
    </div>
  </section>
</body>
</html>
```